Business Card and Logo Color Scheme Design Contest

We are starting a new company called Lone Ridge Structural Partners and already have a logo however, the colors for the logo itself are not final and COULD be changed. I'm hoping to move AWAYfrom the gold color in the card and the logo as it seems a bit outdated. What we need help with is to find what our business color scheme will be, and then incorporate those colors into both the logo and the business card design itself. We also want to make sure we are known as "LRS" so in the future we can just refer to ourselves as "LRS" and not Lone Ridge Structural Partners. That being said, I would like to make a slight change to the logo to somehow include the letters "LRS." The logo used in the front of the card design MUST ALSO include the words "Firm No. 64307" within the logo. My vision is for the front of the card to have the information shown in the attached image. For the back of the card, I'm hoping to have something very simple. I'm envisioning a solid color with either the website (www.bridgemarkplans.com) and a simplified version of the logo. I've attached an example but I'm looking for a complete redesign. I'm looking for a slick, modern and simple design.

Industry/Entity Type

Civil Engineer

Contact Information for Business Card

Logo
Firm No. 64307
Daniel Whitcombe, PE
Chief Operating Officer
Email:dwhitcombe@bridgemarkplans.com
Ph: 936.555.0142 | D: 936.555.0178 | M:210.555.0263
4187 W. Kellingham, Conroe, Texas 77301
www.bridgemarkplans.com

Requirements
Must have
• Logo
Contact Info
Nice to have
• "LRS" Incorporated in the design
Should not have
• The current color scheme

```html
<!DOCTYPE html>
<html lang="en">
<head>
<meta charset="utf-8">
<title>LRS Business Card</title>
<link href="https://fonts.googleapis.com/css2?family=Tinos:wght@400;700&family=Montserrat:wght@400&display=swap" rel="stylesheet">
<style>
  :root {
    --backdrop: #121212;
    --card: #1d1d1d;
    --card-edge: #262626;
    --silver: #c4c4c4;
    --silver-soft: #9a9a9a;
    --silver-dim: #7d7d7d;
  }
  * { margin: 0; padding: 0; box-sizing: border-box; }
  html, body {
    width: 1200px; height: 900px; overflow: hidden;
    background: var(--backdrop);
  }
  .stage {
    position: relative; width: 1200px; height: 900px;
    display: flex; flex-direction: column; align-items: center;
    justify-content: center; gap: 30px;
  }
  .card {
    position: relative; width: 700px; height: 400px;
    background: linear-gradient(135deg, var(--card) 0%, var(--card-edge) 100%);
    box-shadow: 0 18px 40px rgba(0,0,0,0.55);
  }
  /* Front: logo side */
  .card-front {
    display: flex; flex-direction: column; align-items: center; justify-content: center;
  }
  .logo-lockup { display: flex; align-items: center; gap: 16px; }
  .logo-square { width: 54px; height: 54px; background: var(--silver); }
  .logo-name {
    font-family: "Tinos", serif; font-weight: 400; font-size: 72px;
    color: var(--silver); letter-spacing: 2px; line-height: 1;
  }
  .firm-number {
    margin-top: 10px;
    font-family: "Tinos", serif; font-size: 20px; color: var(--silver-soft);
    letter-spacing: 1px;
  }
  .front-company {
    margin-top: 48px;
    font-family: "Tinos", serif; font-size: 26px; color: var(--silver-soft);
  }
  /* Back: contact side */
  .card-back { padding: 56px 40px; }
  .back-company {
    font-family: "Tinos", serif; font-weight: 400; font-size: 38px; color: var(--silver);
    text-align: center; white-space: nowrap;
  }
  .contact-grid {
    display: flex; justify-content: center; margin-top: 56px; align-items: stretch;
  }
  .person { flex: 0 0 270px; text-align: right; padding-right: 24px; }
  .person-name {
    font-family: "Tinos", serif; font-weight: 700; font-size: 25px;
    color: var(--silver-soft); line-height: 1.1; white-space: nowrap;
  }
  .person-title {
    font-family: "Montserrat", sans-serif; font-size: 16px; color: var(--silver-dim);
    margin-top: 4px; white-space: nowrap;
  }
  .person-address {
    font-family: "Montserrat", sans-serif; font-size: 16px; color: var(--silver-dim);
    margin-top: 22px; line-height: 1.5; font-style: normal; white-space: nowrap;
  }
  .divider { flex: 0 0 2px; background: var(--silver-dim); }
  .contact-list { list-style: none; padding-left: 24px; }
  .contact-list li {
    display: flex; align-items: center; gap: 10px;
    font-family: "Montserrat", sans-serif; font-size: 16px; color: var(--silver);
    line-height: 1.65; white-space: nowrap;
  }
  .contact-list svg { width: 14px; height: 14px; flex: none; fill: none; stroke: var(--silver-soft); stroke-width: 1.6; }
</style>
</head>
<body>
<main class="stage">
  <section class="card card-front">
    <div class="logo-lockup">
      <span class="logo-square"></span>
      <span class="logo-name">LRS</span>
    </div>
    <div class="firm-number">Firm No. 64307</div>
    <div class="front-company">Lone Ridge Structural Partners LLC</div>
  </section>

  <section class="card card-back">
    <h1 class="back-company">Lone Ridge Structural Partners LLC</h1>
    <div class="contact-grid">
      <div class="person">
        <div class="person-name">Daniel Whitcombe, PE</div>
        <div class="person-title">Chief Operating Officer</div>
        <address class="person-address">4187 W. Kellingham,<br>Conroe, Texas 77301</address>
      </div>
      <div class="divider"></div>
      <ul class="contact-list">
        <li><svg viewBox="0 0 16 16"><path d="M4 1.5l2.5 3-1.5 1.5c1 2 2.5 3.5 4.5 4.5l1.5-1.5 3 2.5-1.5 2.5C7 14 2 9 1.5 3z"/></svg>936.555.0142</li>
        <li><svg viewBox="0 0 16 16"><rect x="4.5" y="1.5" width="7" height="13" rx="1"/><path d="M7 12.5h2"/></svg>936.555.0178</li>
        <li><svg viewBox="0 0 16 16"><rect x="2" y="6" width="12" height="6" rx="1"/><path d="M4.5 6V2h7v4M4.5 10h7v4h-7z"/></svg>210.555.0263</li>
        <li><svg viewBox="0 0 16 16"><rect x="1.5" y="3.5" width="13" height="9"/><path d="M1.5 3.5l6.5 5 6.5-5"/></svg>dwhitcombe@bridgemarkplans.com</li>
        <li><svg viewBox="0 0 16 16"><circle cx="8" cy="8" r="6.5"/><path d="M1.5 8h13M8 1.5c-3 3.5-3 9.5 0 13M8 1.5c3 3.5 3 9.5 0 13"/></svg>www.bridgemarkplans.com</li>
      </ul>
    </div>
  </section>
</main>
</body>
</html>
```